OTRV - Immigration and Business Consulting Marketing Brochure

81/2 x 11 tri-fold brochure or 11 x 17 tri-fold brochure which ever is suitable to display all our content. Full-colour 4/4,
Immigration and Business Consulting
Present services we provide and web-sites associated with our business. 1st page needs a picture of something related to the first step (choice of picture for your option). Logo would also need to be on this page and contact information page (Logo is uploaded) Uploaded file has all information that we would desire in our brochure. Each section is labeled for your convenience.

Please visit our primary website if you need further information - www.otrv.ca

Target Market(s)

B2B Employers needing Recruitment/Immigration assistance and foreign clients looking to immigrate to Canada.

Industry/Entity Type

Business

Font styles to use
Serif

Requirements
Must have
• Company Logo
Nice to have
• Pictures for specific areas and sections of brochure
Should not have
• Profanity/sexual explicit photos

```html
<!DOCTYPE html>
<html lang="en">
<head>
<meta charset="utf-8">
<title>OTRV Brochure – Inside Spread</title>
<link href="https://fonts.googleapis.com/css2?family=Mulish:wght@300;400&family=Open+Sans:wght@400&family=Oswald:wght@400;500&display=swap" rel="stylesheet">
<style>
  :root{
    --navy:#2f5183;
    --band:#355e91;
    --orange:#ef7a2a;
    --ink:#2b2b2b;
    --paper:#ffffff;
    --blush:#fbf1ea;
  }
  *{box-sizing:border-box;margin:0;padding:0}
  html,body{width:1200px;height:950px;overflow:hidden;background:var(--paper)}
  .spread{position:relative;width:1200px;height:950px;background:linear-gradient(180deg,var(--paper) 40%,var(--blush) 100%);overflow:hidden}
  .photo-row{position:absolute;top:0;left:0;width:1200px;height:330px;display:flex}
  .photo{flex:1;height:100%}
  .photo--nurse{background:linear-gradient(135deg,#c9d4d6 0%,#7fa7c9 45%,#2f6fb3 70%,#d9dcd8 100%)}
  .photo--office{background:linear-gradient(135deg,#f2f0ec 0%,#d7b896 40%,#2a2a2a 65%,#8a8f96 100%)}
  .photo--engineer{background:linear-gradient(135deg,#eef3f8 0%,#c7dbef 45%,#e9a24c 75%,#b8d3ee 100%)}
  .wave{position:absolute;top:0;left:0;width:1200px;height:380px}
  .column{position:absolute;top:345px;width:352px}
  .column--portal{left:34px}
  .column--recruit{left:432px}
  .column--jobs{left:832px}
  .heading{font-family:"Mulish",sans-serif;font-weight:300;line-height:1.15;margin-bottom:26px}
  .heading__lead{display:block;color:var(--orange);font-size:28px}
  .heading__sub{display:block;color:var(--navy);font-size:28px;font-weight:400;letter-spacing:.5px}
  .copy p{font-family:"Open Sans",sans-serif;font-size:14.4px;line-height:18.2px;color:var(--ink);text-align:justify;margin-bottom:6px}
  .visit{position:absolute;top:800px;font-family:"Oswald",sans-serif;color:var(--navy);letter-spacing:2px}
  .visit--portal{left:43px}
  .visit--jobs{left:840px}
  .visit__label{font-size:31px;font-weight:400;line-height:1.1}
  .visit__url{font-size:28px;font-weight:500;line-height:1.2}
  .visit__url .accent{color:var(--orange)}
  .footer-line{position:absolute;left:0;top:902px;width:1200px;height:2px;background:var(--orange)}
  .footer-band{position:absolute;left:0;top:904px;width:1200px;height:46px;background:var(--band)}
</style>
</head>
<body>
<main class="spread">
  <div class="photo-row">
    <div class="photo photo--nurse" role="img" aria-label="Photo of a healthcare worker in blue scrubs reading a tablet"></div>
    <div class="photo photo--office" role="img" aria-label="Photo of a smiling professional woman with colleagues in an office"></div>
    <div class="photo photo--engineer" role="img" aria-label="Photo of an engineer in a white hard hat holding a tablet"></div>
  </div>

  <svg class="wave" viewBox="0 0 1200 380" aria-hidden="true">
    <path d="M0 270 C150 330 330 335 480 318 C700 292 900 250 1200 262 L1200 380 L0 380 Z" fill="#ffffff"/>
    <path d="M0 270 C150 330 330 335 480 318 C700 292 900 250 1200 262 L1200 288 C920 268 700 305 480 330 C320 348 150 345 0 300 Z" fill="#ffffff" opacity=".85"/>
    <path d="M0 262 C150 328 330 335 480 318 C700 292 900 250 1200 262" fill="none" stroke="var(--band)" stroke-width="16"/>
  </svg>

  <section class="column column--portal">
    <h2 class="heading"><span class="heading__lead">Online Application</span><span class="heading__sub">PORTAL</span></h2>
    <div class="copy">
      <p>NomiPort.com is an online application portal that allows OTRV to use reverse logistics to know where workers applications are at during the process. It is a streamlined system that works in coordination with the new provincial nominee and federal online applications.</p>
      <p>NomiPort.com allows foreigner workers to upload their required documents for the application process as well as access information needed through our OTRV professional staff.</p>
      <p>Through live support OTRV’s staff can communicate with workers in real time to answer questions from anywhere in the world and speed up application preparation for quicker submissions.</p>
      <p>The goal of NomiPort.com is to be able to give businesses clients the advantage of an accurate assessments and updates of when workers can arrive to work at their business.</p>
    </div>
  </section>

  <section class="column column--recruit">
    <h2 class="heading"><span class="heading__lead">Employer Recruitment</span><span class="heading__sub">SERVICES</span></h2>
    <div class="copy">
      <p>OTRV works closely with employers to provide the most successful results in recruitment with some of the top talent in the world.</p>
      <p>We at OTRV believe that a labour shortage should be first addressed locally before hiring foreign workers.</p>
      <p>We have set up a successful marketing strategy to find local people by advertising in 10-20 different mediums in western Canada, and by advertising for workers nationally.</p>
      <p>At OTRV we speak the following languages English - Polish - Russian - Ukrainian - Slovak - Czech - Farsi - Spanish - Urdu - Hindi - French - German - Bengali. This helps get a large variety of workers from around the world and it also helps with relocation as well as mediating any issues. OTRV has existing relationships with agents from around the world as well as our own international offices for recruitment purposes.</p>
      <p>OTRV uses a logistical technique, combined with online systems which streamline the recruitment and immigration process while having accurate estimates of when workers can arrive.</p>
    </div>
  </section>

  <section class="column column--jobs">
    <h2 class="heading"><span class="heading__lead">Maple Job</span><span class="heading__sub">HUB</span></h2>
    <div class="copy">
      <p>OTRV has developed a job portal which benefits both the employer and the prospective employees. Utilizing the ability to source skilled workers in Canada and abroad.</p>
      <p>The employer area allows the businesses to match with users that are registered on maplejobhub.ca. This also allows the registered Employer to post and manage jobs opportunities within their companies as well as source through resumes of registered skilled job seekers.</p>
      <p>The potential job seekers (employees) are able to post their resumes as well as update their profile to keep employers aware of the skill level in which the job seeker possesses. Potential employees can access new job opportunities that fit their skill level.</p>
    </div>
  </section>

  <div class="visit visit--portal">
    <div class="visit__label">VISIT</div>
    <div class="visit__url">www.<span class="accent">nomiport</span>.com</div>
  </div>
  <div class="visit visit--jobs">
    <div class="visit__label">VISIT</div>
    <div class="visit__url">www.<span class="accent">maplejobhub</span>.ca</div>
  </div>

  <div class="footer-line"></div>
  <div class="footer-band"></div>
</main>
</body>
</html>
```